Brightwell Wiring Needs A Logo Design

We need a logo for my new company based out of Sacramento, Ca called Brightwell Wiring. The name says it all, my electrical contracting business provides "Brightwell Craftsman Work" I'm open to any colors that pop and customers to say Wow. I would love to print my cards on metal.

Contact Information for Business Card

The card needs to have as follows
Name of company: Brightwell Wiring
My Name: Marco Delvane
Phone # 916-555-0147
CL# 4873920
Email: brightwellwiring@mailtorva.com
and a slogan that represent "BRIGHTWELL"

Requirements
Must have
• The card needs to have as follows
• Name of company: Brightwell Wiring
• My Name : Marco Delvane
• Phone # 916-555-0147
• CL# 4873920
• Email: brightwellwiring@mailtorva.com
• and a slogan that represent "BRIGHTWELL"
Nice to have
• popping colors
• electrical Arcing

```html
<!DOCTYPE html>
<html lang="en">
<head>
<meta charset="utf-8">
<title>Brightwell Wiring – Business Card</title>
<link rel="stylesheet" href="https://fonts.googleapis.com/css2?family=Lato:wght@400&family=Marcellus+SC&display=swap">
<style>
  :root {
    --backdrop: #5b3d3f;
    --card-navy: #0f1126;
    --card-deep: #0b0d1b;
    --glow-blue: rgba(52, 72, 210, 0.75);
    --glow-soft: rgba(40, 55, 180, 0.35);
    --glow-core: #eef2ff;
    --accent-yellow: #f3e500;
    --text-white: #ffffff;
  }
  * { margin: 0; padding: 0; box-sizing: border-box; }
  html, body { width: 1200px; height: 1200px; overflow: hidden; }
  body {
    background: var(--backdrop);
    position: relative;
    font-family: "Lato", sans-serif;
    color: var(--text-white);
  }
  .card {
    position: absolute;
    left: 190px;
    width: 818px;
    height: 464px;
    background: var(--card-navy);
    overflow: hidden;
    box-shadow: 0 6px 14px rgba(0,0,0,0.45);
  }
  .card--front { top: 96px; }
  .card--back { top: 654px; }

  /* soft glow standing in for the electric arc artwork */
  .arc-art {
    position: absolute;
    inset: 0;
  }
  .arc-art--front {
    background:
      radial-gradient(circle 70px at 410px 118px, var(--glow-core) 0%, rgba(200,212,255,0.75) 25%, rgba(90,110,240,0.35) 60%, rgba(15,17,38,0) 100%),
      radial-gradient(ellipse 470px 70px at 560px 120px, var(--glow-blue) 0%, var(--glow-soft) 50%, rgba(15,17,38,0) 100%),
      radial-gradient(ellipse 320px 170px at 410px 130px, rgba(40,55,180,0.55) 0%, rgba(15,17,38,0) 100%),
      radial-gradient(ellipse 620px 230px at 440px 150px, rgba(30,40,140,0.45) 0%, rgba(15,17,38,0) 100%);
  }
  .arc-art--back {
    background:
      radial-gradient(circle 80px at 409px 226px, var(--glow-core) 0%, rgba(200,212,255,0.75) 25%, rgba(90,110,240,0.35) 60%, rgba(15,17,38,0) 100%),
      radial-gradient(ellipse 640px 70px at 409px 228px, var(--glow-blue) 0%, var(--glow-soft) 55%, rgba(15,17,38,0) 100%),
      radial-gradient(ellipse 300px 190px at 409px 240px, rgba(40,55,180,0.55) 0%, rgba(15,17,38,0) 100%),
      radial-gradient(ellipse 720px 150px at 409px 232px, rgba(30,40,150,0.55) 0%, rgba(15,17,38,0) 100%);
  }

  .brand-band {
    position: absolute;
    left: 0; top: 83px;
    width: 380px; height: 63px;
    background: linear-gradient(90deg, rgba(70,85,200,0.3) 0%, rgba(70,85,200,0.22) 70%, rgba(70,85,200,0) 100%);
  }
  .brand-name {
    position: absolute;
    left: 33px; top: 94px;
    font-family: "Marcellus SC", serif;
    font-weight: 400;
    font-size: 34px;
    letter-spacing: 2px;
    line-height: 40px;
    color: var(--text-white);
    white-space: nowrap;
  }

  .owner {
    position: absolute;
    left: 0; width: 100%;
    top: 225px;
    text-align: center;
    line-height: 1;
  }
  .owner__name { font-size: 35px; display: block; }
  .owner__title { font-size: 22px; display: block; margin-top: 4px; }

  .divider {
    position: absolute;
    left: 170px; top: 307px;
    width: 517px; height: 2px;
    background: linear-gradient(90deg, rgba(255,255,255,0.2) 0%, var(--accent-yellow) 10%, var(--accent-yellow) 90%, rgba(255,255,255,0.2) 100%);
  }

  .contact-strip {
    position: absolute;
    left: 0; bottom: 0;
    width: 100%; height: 96px;
    background: var(--card-deep);
  }
  .contact-list {
    position: absolute;
    left: 44px; top: 4px;
    list-style: none;
    font-size: 23px;
    line-height: 28px;
  }
  .contact-list li { display: flex; align-items: center; gap: 12px; }
  .contact-icon { width: 21px; height: 20px; flex: none; }
  .license {
    position: absolute;
    right: 42px; top: 32px;
    font-size: 23px;
    line-height: 28px;
  }
  .license__label { color: var(--accent-yellow); }

  .slogan {
    position: absolute;
    left: 0; width: 100%;
    top: 394px;
    text-align: center;
    font-size: 24px;
  }
</style>
</head>
<body>

  <section class="card card--front" aria-label="Business card front">
    <div class="arc-art arc-art--front" role="img" aria-label="Electric arc with a glowing spark burst"></div>
    <div class="brand-band"></div>
    <h1 class="brand-name">Brightwell Wiring</h1>

    <p class="owner">
      <span class="owner__name">Marco Delvane</span>
      <span class="owner__title">CEO</span>
    </p>

    <div class="divider"></div>

    <div class="contact-strip">
      <ul class="contact-list">
        <li>
          <svg class="contact-icon" viewBox="0 0 21 20" aria-hidden="true">
            <path d="M1 7 Q10.5 0 20 7 L17 9 L14 7 L14 5 Q10.5 3.5 7 5 L7 7 L4 9 Z" fill="#f3e500"/>
            <path d="M4 10 L7 8 L14 8 L17 10 L19 19 L2 19 Z" fill="#f3e500"/>
            <circle cx="10.5" cy="13.5" r="3" fill="#0b0d1b"/>
            <circle cx="10.5" cy="13.5" r="1.2" fill="#f3e500"/>
          </svg>
          <span>916-555-0147</span>
        </li>
        <li>
          <svg class="contact-icon" viewBox="0 0 21 20" aria-hidden="true">
            <rect x="1" y="3" width="19" height="14" fill="#f3e500"/>
            <path d="M2 4 L10.5 11 L19 4 M2 16 L8 9.5 M19 16 L13 9.5" fill="none" stroke="#0b0d1b" stroke-width="1.6"/>
          </svg>
          <span>brightwellwiring@mailtorva.com</span>
        </li>
      </ul>
      <p class="license"><span class="license__label">CL#</span> 4873920</p>
    </div>
  </section>

  <section class="card card--back" aria-label="Business card back">
    <div class="arc-art arc-art--back" role="img" aria-label="Horizontal electric arc across the card with a bright spark burst at its centre"></div>
    <p class="slogan">Brightwell Craftsman Work</p>
  </section>

</body>
</html>
```